Webdesign für Beratung und Service im Bereich Heizungs- und Kühltechnologie
Zielgruppe
Wir sind ein modernes Dienstleistungsunternehmen, dass im Bereich Beratung und Service für Heizungs- und Kühltechnologie tätig ist. Wir suchen ein modernes Webdesign, das sich überwiegend an Geschäfts- / Gewerbekunden richten soll.
Aufgabenstellung
Wir möchten die in unserem Logo verwendete Farben auf der Webseite wiederfinden, Bilder werden mitgeliefert, müssen aber keine Verwendung finden. Wichtig ist das Hervorheben als Kundendienstvertretung des Premium-Herstellers BRK mit deren Logo und direktem Link auf deren Webseite. Gerne würden wir einen modernen Ansatz sehen, abweichend von den Standard-Seiten anderer Wartungsfirmen in unserer Branche.

```html
<!DOCTYPE html>
<html lang="de">
<head>
<meta charset="utf-8">
<title>Thermova – Heizungs- und Kühltechnologie</title>
<link href="https://fonts.googleapis.com/css2?family=Open+Sans:ital,wght@0,400;0,600;0,700;1,700&display=swap" rel="stylesheet">
<style>
:root{
  --navy:#1c3260;
  --navy-dark:#13305f;
  --red:#c4252c;
  --red-dark:#8f1d22;
  --alert:#e0202a;
  --band:#c4cfdc;
  --text:#1f3a6e;
  --line:#8a9bb8;
  --muted:#6b7690;
  --white:#fff;
}
*{box-sizing:border-box;margin:0;padding:0}
html,body{width:1200px;height:2312px;overflow:hidden;background:var(--white);font-family:"Open Sans",Arial,sans-serif;color:var(--text)}
.page{position:relative;width:1200px;height:2312px;overflow:hidden}
.abs{position:absolute}

/* header */
.brand{left:220px;top:14px;display:flex;align-items:center;gap:8px}
.brand-mark{width:18px;height:18px;border-radius:50%;background:var(--navy);display:block}
.brand-name{font-size:22px;font-weight:700;color:var(--navy);line-height:1}
.tagline{left:358px;top:15px;font-size:11.5px;font-weight:600;color:var(--navy);text-align:center;line-height:15px}
.topbar{right:165px;top:9px;font-size:7.5px;color:var(--navy);display:flex;gap:26px}
.topbar .hot{color:var(--red-dark);font-weight:700}
.mainnav{right:165px;top:32px;display:flex;gap:15px;font-size:9.5px;color:var(--navy)}
.mainnav .active{font-weight:700}

/* hero */
.hero{left:0;top:56px;width:1200px;height:563px;overflow:hidden;background:linear-gradient(90deg,#8d9197 0%,#b6babf 20%,#a3a7ac 50%,#b2b6bb 80%,#8d9197 100%)}
.hero-fan{left:455px;top:20px;width:420px;height:420px;border-radius:50%;background:radial-gradient(circle at 50% 50%,#d4a25a 0%,#7a6446 30%,#3d3b38 55%,#6f7276 68%,#b3b6ba 72%)}
.hero-title{left:255px;top:130px;font-size:31px;font-weight:700;color:var(--white);line-height:38px}
.btn-emergency{left:276px;top:318px;height:28px;width:163px;background:var(--alert);color:var(--white);font-weight:700;font-size:18px;letter-spacing:.5px;display:flex;align-items:center;gap:8px;padding-left:8px}

/* cards */
.band{left:0;top:881px;width:1200px;height:249px;background:var(--band)}
.card{top:569px;width:226px;height:362px;background:var(--white);border:1px solid var(--line);text-align:center;padding:16px 12px 0;overflow:hidden}
.card h2{font-size:19px;font-weight:600;color:var(--navy);margin:6px 0 10px;line-height:24px}
.card p{font-size:9px;line-height:13.7px;color:var(--text)}
.card-icon{height:38px;display:flex;justify-content:center;align-items:flex-end}
.partner{display:flex;align-items:center;gap:5px;font-size:22px;font-weight:700;color:var(--red);line-height:1}
.partner i{width:8px;height:8px;background:var(--red);display:block}
.product{top:937px;height:310px}

/* emergency */
.emergency{left:0;top:1272px;width:1200px;text-align:center}
.emergency h3{font-size:19px;font-weight:600;color:var(--red-dark);display:flex;justify-content:center;align-items:center;gap:8px}
.emergency p{font-size:9px;line-height:13.7px;margin-top:4px;color:var(--navy)}
.emergency b{font-weight:700}

/* contact */
.contact{left:0;top:1374px;width:1200px;text-align:center}
.contact h3{font-size:19px;font-weight:600;color:var(--red-dark)}
.contact .intro{font-size:9px;margin-top:8px;color:var(--navy);display:flex;justify-content:center;align-items:center;gap:5px}
.box{display:inline-block;width:10px;height:10px;border:1px solid var(--navy);flex:none}
.field{top:1432px;width:131px;height:18px;border:1px solid var(--line);font-size:6.5px;color:#8791a5;padding:4px 8px}
.hint{font-size:6.5px;color:var(--muted)}
.textarea{left:244px;top:1474px;width:416px;height:39px;border:1px solid var(--line)}
.consent{left:255px;top:1532px;font-size:6.5px;line-height:12px;color:var(--muted);display:flex;gap:8px}
.consent u{text-decoration:underline}
.submit{left:675px;top:1534px;width:100px;height:18px;background:var(--navy-dark);color:var(--white);font-size:10.5px;text-align:center;line-height:18px}

/* footer */
.footer{left:0;top:1587px;width:1200px;height:126px;background:var(--navy-dark)}
.footnav{left:420px;top:1617px;font-size:7.5px;font-weight:700;color:var(--white);line-height:13px}
.footlogo{left:527px;top:1616px;width:140px;height:44px;background:var(--white);display:flex;align-items:center;justify-content:center;gap:6px}
.footlogo .brand-name{font-size:18px}
.foottag{left:527px;top:1664px;width:140px;text-align:center;font-size:9.5px;font-weight:600;color:var(--white);line-height:15px}
.address{left:729px;top:1617px;font-size:7.5px;font-weight:700;color:var(--white);line-height:13px}
.cookie{left:0;top:1674px;width:1200px;height:38px;background:rgba(150,160,178,.75);display:flex;align-items:center;justify-content:center;gap:12px;font-size:8.5px;color:var(--navy)}
.cookie .ok{background:var(--navy-dark);color:var(--white);font-weight:700;font-size:14px;width:36px;height:30px;text-align:center;line-height:30px;letter-spacing:1px}

/* mobile layout */
.mobile{left:244px;top:1810px;width:202px;height:361px;border:1px solid #d3d8e0;overflow:hidden;background:var(--white)}
.m-top{height:18px;display:flex;justify-content:space-between;align-items:center;padding:0 10px;font-size:6px;color:var(--navy)}
.m-top .hot{color:var(--red-dark);font-weight:700}
.m-hero{height:120px;background:radial-gradient(circle at 50% 50%,#d4a25a 0%,#7a6446 28%,#3d3b38 48%,#9a9ea3 62%,#b6babf 100%)}
.m-btn{margin:-11px auto 0;width:132px;height:22px;background:var(--alert);color:var(--white);font-weight:700;font-size:14px;display:flex;align-items:center;gap:6px;padding-left:6px;position:relative}
.m-title{text-align:center;font-size:13px;font-weight:600;color:var(--navy);line-height:19px;margin-top:8px}
.m-about{text-align:center;margin-top:8px}
.m-about h4{font-size:13px;font-weight:600;color:var(--navy)}
.m-about p{font-size:8.5px;line-height:13px;color:var(--navy)}
.m-menu{position:absolute;left:0;bottom:0;width:100%;height:22px;background:var(--navy-dark);display:flex;align-items:center;justify-content:space-between;padding:0 12px;color:var(--white);font-size:8px;font-weight:700;letter-spacing:2px}
.m-menu .m-brand{background:var(--white);color:var(--navy);border-radius:8px;padding:1px 8px;font-size:7px;letter-spacing:0}
</style>
</head>
<body>
<div class="page">

  <!-- header -->
  <div class="abs brand"><span class="brand-mark"></span><span class="brand-name">Thermova</span></div>
  <div class="abs tagline">HIGH EFFICIENT HEATING<br>AND COOLING SERVICE</div>
  <div class="abs topbar"><span>✉ info@thermova.de</span><span><span class="hot">Notdienst</span> ☏ +49 (0) 4711 5520 22</span></div>
  <nav class="abs mainnav"><span class="active">Home</span><span>Über uns</span><span>Kundendienst BRK</span><span>Wartung</span><span>Notdienst</span><span>Kontakt</span></nav>

  <!-- hero -->
  <div class="abs hero" role="img" aria-label="Foto eines Lüftungsgitters mit Ventilator in einer Metallwand">
    <div class="abs hero-fan"></div>
  </div>
  <h1 class="abs hero-title">Ihr Spezialist für<br>Beratung und Service<br>im Bereich der<br>Heizungs- und Kühltechnologie</h1>
  <div class="abs btn-emergency">
    <svg width="20" height="20" viewBox="0 0 20 20" fill="none" stroke="#fff" stroke-width="1.4"><circle cx="10" cy="10" r="9"/><path d="M5 6c0 5 4 9 9 9l1-2-3-1-1 1c-2-1-3-2-4-4l1-1-1-3z"/></svg>
    NOTDIENST
  </div>

  <!-- service cards -->
  <div class="abs band"></div>

  <section class="abs card" style="left:238px">
    <div class="card-icon"><svg width="40" height="38" viewBox="0 0 40 38" fill="none" stroke="#c4252c" stroke-width="2.4"><path d="M3 18L20 3l17 15"/><path d="M8 14v21h8V23h8v12h8V14"/></svg></div>
    <h2>Über uns</h2>
    <p>Wir sind ein modernes Beratungs- und Service-Unternehmen mit hochmotivierten Mitarbeitern, die seit Jahrzehnten in der Heizungs- und Klimabranche tätig sind. Unsere Mitarbeiter sind stets auf den neuesten Stand der Technik geschult. Verteilte Servicestationen machen es möglich, dass wir Ihnen deutschlandweit an 365 Tagen / 24 Stunden unsere Dienste anbieten können. Optimierte Einsatzplanung garantieren Ihnen schnelle Reaktionszeiten und schlanke Prozessstrukturen sorgen für eine reibungslose Ersatzteilversorgung. Profitieren Sie von dem tiefgreifenden Know-How unsere Mitarbeiter, ihren langjährigen Erfahrungen und dem hohen Qualitätsanspruch unseres Unternehmens.</p>
  </section>

  <section class="abs card" style="left:487px">
    <div class="card-icon"><span class="partner"><i></i>BRK</span></div>
    <h2>Kundendienst</h2>
    <p>In unserem Fokus stehen Heizungs- und Kühltechnologie mit hoher Effizienz und Rückhaltigkeit.<br>Als Kundendienstvertretung des <b><i>Schweizer Premium-Herstellers BRK</i></b>, übernehmen wir alle Kundendienstleistungen für Inbetriebnahmen, Gewährleistungs- Wartungs- und Servicearbeiten für deren Produktportfolio (u.a. Luft-Wasser oder Sole-Wasser Wärmepumpen, Splitgeräte und Serverraumkühlungen).<br>Außerdem bieten wir Service und Wartungsarbeiten für folgende Produkte an:<br>• Klimaanlagen der Firma Nordkalt<br>• Ferrano-Wärmepumpen<br>• Heizungswartungen und Austausch an Brennwald, Vitherm, Valtaro etc.<br>• Solaranlagen<br>• BHKW der Firmen KMT und Enerwerk</p>
  </section>

  <section class="abs card" style="left:737px">
    <div class="card-icon"><svg width="40" height="38" viewBox="0 0 40 38" fill="none" stroke="#c4252c" stroke-width="2.2"><path d="M6 32L30 8l4-4 3 3-4 4L9 35z"/><path d="M34 32L12 10a6 6 0 0 0-8-7l4 4-2 3-4-2a6 6 0 0 0 7 7l22 22z"/></svg></div>
    <h2>Wartung-Service</h2>
    <p>• Sorgt für einen störungsfreien Regel-Betrieb<br>• Steht für eine optimale Energiebilanz<br>• Verlängert die Lebensdauer Ihrer Anlage<br>• Erfüllt die gesetzl. Betriebsanforderungen<br><br>Unsere Wartungs-Service umfasst:<br>• Kontrolle des gesamten Systems<br>• Austausch von Verschleißteilen<br>• Einstellung der Betriebsparameter<br>• Erkennen von Fehlern bevor diese ein Problem werden<br>• Sauberes, Arbeiten und transparente Information an den Kunden<br><br>Wartungsverträge nach FTKV schaffen Sicherheit und Vertrauen - entschieden Sie sich für den Spezialisten und lassen Sie sich ein individuelles Angebot für Ihre Anlagen erstellen</p>
  </section>

  <div class="abs product" style="left:225px;width:225px;background:linear-gradient(90deg,#b8bbbf,#e6e7e9 45%,#c9cbce)" role="img" aria-label="Produktfoto einer silbernen Außeneinheit-Wärmepumpe"></div>
  <div class="abs product" style="left:482px;width:200px;background:linear-gradient(90deg,#2a2a2c,#6a5040 50%,#303033)" role="img" aria-label="Produktfoto einer geöffneten Wärmepumpe mit Kupferleitungen"></div>
  <div class="abs product" style="left:700px;width:285px;top:945px;height:280px;background:linear-gradient(90deg,#b3b5b8,#e8e9ea 50%,#8c8e91)" role="img" aria-label="Produktfoto einer silbernen Innen-Wärmepumpe"></div>

  <!-- emergency -->
  <section class="abs emergency">
    <h3><svg width="36" height="36" viewBox="0 0 36 36" fill="none" stroke="#8f1d22" stroke-width="1.4"><circle cx="22" cy="14" r="12"/><path d="M4 10c0 12 10 22 22 22l2-4-5-3-3 2c-4-2-7-5-9-9l2-3-3-5z"/><text x="16" y="18" font-size="10" fill="#8f1d22" stroke="none" font-family="Open Sans">24</text></svg>Notdienst +49 (0) 4711 5520 22</h3>
    <p>Unser Notdienst steht Ihnen rund-um die Uhr für folgende Leistungen zur Verfügung:<br>Identifizieren und Beheben von Betriebs-Störungen an:<br><b>• Wärmepumpen &nbsp;&nbsp;&nbsp;• Heizungsanlagen &nbsp;&nbsp;&nbsp;• Klimaanlagen &nbsp;&nbsp;• Solaranlagen</b></p>
  </section>

  <!-- contact -->
  <section class="abs contact">
    <h3>Kontakt zu uns</h3>
    <div class="intro">Bitte nehmen Sie zu mit / uns unverbindlich Kontakt auf, wir möchte uns beraten lassen zu Ihren <span class="box"></span> BRK-Servicearbeiten &nbsp;<span class="box"></span> BRK-Wartungsarbeiten <span class="box"></span> sonstiger Hersteller</div>
  </section>
  <div class="abs field" style="left:245px">Name, Vorname*</div>
  <div class="abs field" style="left:386px">Firma*</div>
  <div class="abs field" style="left:529px">E-Mailadresse*</div>
  <div class="abs field" style="left:674px">Tel. / Handy*</div>
  <div class="abs field" style="left:820px">Gerätestandort</div>
  <div class="abs hint" style="left:255px;top:1462px">Bitte teilen Sie uns in Ihrer Nachricht nach Möglichkeit genauer Informationen zu Hersteller, Gerätetyp, Baujahr, Garantie und / oder Mängel mit.</div>
  <div class="abs hint" style="left:827px;top:1462px">*Pflichtfelder</div>
  <div class="abs textarea"></div>
  <div class="abs consent"><span class="box" style="margin-top:2px"></span><span>Ich habe die <u>Datenschutzerklärung</u> zur Kenntnis genommen und akzeptiert. Ich stimme zu, dass meine<br>Formularangaben zur Kontaktaufnahme bzw. zur Bearbeitung meines Anliegens gespeichert werden.</span></div>
  <div class="abs submit">abschicken &gt;</div>

  <!-- footer -->
  <footer class="abs footer"></footer>
  <div class="abs footnav">Home<br>Kontakt<br>Impressum<br>AGB<br>Datenschutz<br>Cookie-Policy</div>
  <div class="abs footlogo"><span class="brand-mark" style="width:14px;height:14px"></span><span class="brand-name">Thermova</span></div>
  <div class="abs foottag">HIGH EFFICIENT HEATING<br>AND COOLING SERVICE</div>
  <div class="abs address">Thermova GmbH<br>Lindenweg 5b<br>84219 Auenried-Lindach<br>Tel. +49 (0) 4711 5520 22<br>Fax +49 (0) 4711 5520 23<br>info@thermova.de</div>
  <div class="abs cookie"><span>Um unsere Webseite für Sie optimal zu gestalten und fortlaufend verbessern zu können, verwenden wir Cookies. Durch die weitere Nutzung der Webseite stimmen Sie der Verwendung von Cookies zu.</span><span class="ok">OK</span></div>

  <!-- mobile layout -->
  <div class="abs mobile">
    <div class="m-top"><span>✉</span><span><span class="hot">Notdienst</span> ☏ +49 (0) 4711 5520 22</span></div>
    <div class="m-hero" role="img" aria-label="Foto eines Lüftungsgitters mit Ventilator"></div>
    <div class="m-btn"><svg width="16" height="16" viewBox="0 0 20 20" fill="none" stroke="#fff" stroke-width="1.4"><circle cx="10" cy="10" r="9"/><path d="M5 6c0 5 4 9 9 9l1-2-3-1-1 1c-2-1-3-2-4-4l1-1-1-3z"/></svg>NOTDIENST</div>
    <div class="m-title">Ihr Spezialist für<br>Beratung und Service<br>im Bereich der<br>Heizungs- und Kühltechnologie</div>
    <div class="m-about">
      <svg width="34" height="32" viewBox="0 0 40 38" fill="none" stroke="#c4252c" stroke-width="2.4"><path d="M3 18L20 3l17 15"/><path d="M8 14v21h8V23h8v12h8V14"/></svg>
      <h4>Über uns</h4>
      <p>Wir sind ein modernes Beratungs- und<br>Service-Unternehmen mit hochmotivierten</p>
    </div>
    <div class="m-menu"><span>☰ MENU</span><span class="m-brand">Thermova</span></div>
  </div>

</div>
</body>
</html>
```